Board to put on a meditation centre - Lantern Grove

I need a board design for a new meditation centre based in Oslo which offers free courses in meditation and self-empowerment. The size of the board is width 374cm x height 104cm.  The name of the meditation centre together with subtitles should be on the board but also some elegant decoration that matches the theme (lantern grove/meditation).
Here is the website of the meditation centre to give you a feeling of it: https://lyktelundsenteret.no/
Good if you can use a blue color close to this one: rgb(37, 180, 193) as well as some brown/golden color (similar to the palette on the website).
On the board it should say:
Lyktelunden (in big letters, the rest is subtitles)
Meditasjon & Spirituell visdom
Kurs - Retreat - Dialog
lyktelundsenteret.no
The design should be very elegant and beautiful and the feeling should be of "An Lantern Grove". A logo is here attached and should be used but I need to get a better quality version of it, will upload that as soon as possible.

```html
<!DOCTYPE html>
<html lang="no">
<head>
<meta charset="utf-8">
<title>Lyktelunden – skilt</title>
<link rel="stylesheet" href="https://fonts.googleapis.com/css2?family=Raleway:wght@400;500;600&display=swap">
<style>
  :root {
    --backdrop: #d7b94a;
    --teal: #25afbe;
    --gold: #d2b23f;
    --white: #ffffff;
    --accent: #c51f3a;
  }
  html, body {
    margin: 0;
    padding: 0;
    width: 1200px;
    height: 519px;
    overflow: hidden;
    background: var(--backdrop);
  }
  .canvas {
    position: relative;
    width: 1200px;
    height: 519px;
  }
  .board {
    position: absolute;
    left: 40px;
    top: 104px;
    width: 1120px;
    height: 311px;
    font-family: "Raleway", sans-serif;
    text-align: center;
  }
  .board-frame {
    position: absolute;
    inset: 0;
    width: 100%;
    height: 100%;
  }
  .board-frame .band { fill: var(--teal); }
  .board-frame .panel { fill: var(--white); }
  .board-frame .trim { fill: none; stroke: var(--gold); stroke-width: 3; }
  .mark-dot {
    position: absolute;
    left: 50%;
    top: 30px;
    width: 74px;
    height: 74px;
    margin-left: -37px;
    border-radius: 50%;
    background: var(--accent);
  }
  .name {
    position: absolute;
    left: 0;
    right: 0;
    top: 103px;
    margin: 0;
    color: var(--teal);
    font-weight: 500;
    font-size: 84px;
    line-height: 1;
    letter-spacing: -0.01em;
  }
  .tagline {
    position: absolute;
    left: 0;
    right: 0;
    top: 190px;
    margin: 0;
    color: var(--gold);
    font-weight: 400;
    font-size: 33px;
    line-height: 1;
  }
  .offerings {
    position: absolute;
    left: 372px;
    width: 376px;
    top: 235px;
    height: 31px;
    margin: 0;
    border-top: 1px solid var(--gold);
    border-bottom: 1px solid var(--gold);
    box-sizing: border-box;
    color: var(--teal);
    font-weight: 500;
    font-size: 20px;
    letter-spacing: 0.2em;
    line-height: 29px;
  }
  .web {
    position: absolute;
    left: 0;
    right: 0;
    top: 277px;
    margin: 0;
    color: var(--gold);
    font-weight: 500;
    font-size: 15px;
    letter-spacing: 0.24em;
    line-height: 1;
  }
</style>
</head>
<body>
<main class="canvas">
  <section class="board">
    <svg class="board-frame" viewBox="0 0 1526 424" preserveAspectRatio="none" aria-hidden="true">
      <rect class="band" x="0" y="0" width="1526" height="424"/>
      <path class="panel" d="M240,0 C160,50 130,190 57,209 C140,240 190,400 257,424 H1280 C1342,400 1382,240 1467,209 C1402,190 1362,40 1277,0 Z"/>
      <path class="trim" d="M302,0 C202,30 172,190 100,209 C182,235 222,410 328,424"/>
      <path class="trim" d="M1202,0 C1322,30 1362,190 1427,209 C1352,235 1312,410 1210,424"/>
    </svg>
    <div class="mark-dot" aria-hidden="true"></div>
    <h1 class="name">Lyktelunden</h1>
    <p class="tagline">Meditasjon &amp; Spirituell Visdom</p>
    <p class="offerings">KURS - RETREAT - DIALOG</p>
    <p class="web">lyktelundsenteret.no</p>
  </section>
</main>
</body>
</html>
```